Business Card Design

I am a criminologist running a research and consultancy business on my own (PKConsultants)
I specialise in looking at fraud and other white-collar crimes. Also governance issues..
I would like a professional business card that would be appropriate both in the academic and business sector as I straddle both sectors. Normal shape - not square.
I am interested in seeing border Word Cloud type projects - black on white or white on black..
Example key words would be fraud, research, qualitative, interviews, quantitative, white-collar, reports, government, surveys, sample, governance, assurance, crime, offenders, prison etc (I can provide a full list if this is the option I go for). I also like Word Cloud borders as attached.
I am also interested in seeing other style business cards. Preferably one colour, plus black and white.
In particular I like black backgrounds with coloured words etc - colours like lime green are good.
I also like blues - especially teal if a traditional white background is chosen.
I don't have a logo - unless anyone can think of anything that's particularly appropriate.
Graphics can be used but they would be simple and stylish (dots, squares, lines, curves etc)
I would like the design to translate simply for a header for a website or blog.
My current website is www.pelling-hurst.com but is out of date in terms of what I do and design.
I have attached a number of things that have caught my eye and inspired me.
I have asked for a one-sided business card in the first instance - however if someone comes up with a good cloud design that might go on one side, I would consider a two-sided one.
Design can be landscape or portrait.
Kind Regards
Meg
Landscape
Contact Information for Business Card
PKConsultants
Dr Margery Pelling-Hurst, MSc, BSc, **
42 Brindle Wold
Stone, Staffordshire
KX27 4QD
+44(0)1620 482917
+44(0)7531 804152
www.pelling-hurst.com
margery@pelling-hurst.com

```html
<!DOCTYPE html>
<html lang="en">
<head>
<meta charset="utf-8">
<title>PK Consultants – Business Card</title>
<link rel="stylesheet" href="https://fonts.googleapis.com/css2?family=Marcellus+SC&family=Open+Sans:wght@400;600&display=swap">
<style>
  :root {
    --bg: #e9e6e1;
    --card-dark: #1c1c1c;
    --card-mid: #333333;
    --lime: #9fd23f;
    --lime-light: #c2e86a;
    --lime-deep: #7fb02a;
    --ink-on-lime: #232323;
    --text-light: #e8e8e8;
    --icon-bg: #5a5a5a;
  }
  * { box-sizing: border-box; margin: 0; padding: 0; }
  html, body { width: 1200px; height: 1023px; overflow: hidden; }
  body {
    background: var(--bg);
    position: relative;
    font-family: "Open Sans", Arial, sans-serif;
  }
  .card {
    position: absolute;
    width: 700px;
    height: 400px;
    border-radius: 6px;
    overflow: hidden;
    background: linear-gradient(120deg, var(--card-mid) 0%, var(--card-dark) 70%);
    box-shadow: 0 10px 30px rgba(0,0,0,.25);
  }
  .card--front { left: 90px; top: 70px; }
  .card--back { left: 410px; top: 545px; }

  .front-rule {
    position: absolute;
    left: 0; right: 0; top: 138px;
    height: 4px;
    background: var(--lime);
  }
  .front-band {
    position: absolute;
    left: 0; right: 0; top: 150px;
    height: 120px;
    background: linear-gradient(90deg, var(--lime) 0%, var(--lime-light) 100%);
  }
  .front-edge {
    position: absolute;
    left: 0; right: 0; bottom: 0;
    height: 8px;
    background: var(--lime-deep);
  }

  .brand {
    position: absolute;
    left: 40px; top: 44px;
    display: flex; align-items: center; gap: 16px;
  }
  .brand__dot {
    width: 40px; height: 40px; border-radius: 50%;
    border: 5px solid var(--lime);
  }
  .brand__name {
    font-family: "Marcellus SC", Georgia, serif;
    font-size: 42px;
    line-height: 1;
    color: var(--lime);
    letter-spacing: 1px;
  }

  .person {
    position: absolute;
    left: 40px; top: 176px;
    color: var(--ink-on-lime);
  }
  .person__name {
    font-family: "Marcellus SC", Georgia, serif;
    font-size: 28px;
    line-height: 1.2;
  }
  .person__role { font-size: 14px; margin-top: 4px; }

  .address {
    position: absolute;
    right: 40px; top: 172px;
    text-align: right;
    font-size: 15px;
    line-height: 1.6;
    color: var(--ink-on-lime);
  }
  .address__web { font-weight: 600; }

  .contacts {
    position: absolute;
    left: 40px; top: 290px;
    list-style: none;
    font-size: 15px;
    line-height: 1.7;
    color: var(--text-light);
  }
  .contacts li { display: flex; align-items: center; gap: 10px; }
  .contacts svg { width: 16px; height: 16px; flex: none; }

  .back-name {
    position: absolute;
    left: 0; right: 0; top: 170px;
    text-align: center;
    font-family: "Marcellus SC", Georgia, serif;
    font-size: 46px;
    color: var(--lime);
    letter-spacing: 1px;
  }
</style>
</head>
<body>

<section class="card card--front" aria-label="Business card front">
  <div class="front-rule"></div>
  <div class="front-band"></div>
  <div class="front-edge"></div>

  <div class="brand">
    <span class="brand__dot"></span>
    <span class="brand__name">PK Consultants</span>
  </div>

  <div class="person">
    <p class="person__name">Dr Margery</p>
    <p class="person__role">Pelling-Hurst, MSc, BSc</p>
  </div>

  <p class="address">
    42 Brindle Wold Stone<br>
    Staffordshire KX27 4QD<br>
    <span class="address__web">www.pelling-hurst.com</span>
  </p>

  <ul class="contacts">
    <li>
      <svg viewBox="0 0 16 16"><rect width="16" height="16" rx="2" fill="#5a5a5a"/><path d="M5 4l2 2-1 1c.5 1 1.5 2 3 3l1-1 2 2-1.5 1.5C7 12 4 9 3.5 5.5z" fill="#e8e8e8"/></svg>
      +44(0)1620 482917
    </li>
    <li>
      <svg viewBox="0 0 16 16"><rect width="16" height="16" rx="2" fill="#5a5a5a"/><rect x="5" y="3" width="6" height="10" rx="1" fill="none" stroke="#e8e8e8" stroke-width="1.2"/></svg>
      +44(0)7531 804152
    </li>
    <li>
      <svg viewBox="0 0 16 16"><rect width="16" height="16" rx="2" fill="#5a5a5a"/><rect x="3" y="5" width="10" height="7" fill="none" stroke="#e8e8e8" stroke-width="1.2"/><path d="M3 5l5 4 5-4" fill="none" stroke="#e8e8e8" stroke-width="1.2"/></svg>
      margery@pelling-hurst.com
    </li>
  </ul>
</section>

<section class="card card--back" aria-label="Business card back">
  <p class="back-name">PK Consultants</p>
</section>

</body>
</html>
```